Business Card Design Project

Need a business card with logo that is attached.
Company name: Moberly Swift Solutions, LLC
My name: Lucia Pembrook
Title: President
Phone number: 703-482-1947
Email: lpembrook@moberlyswiftsolutions.example
web site: www.moberlyswiftsolutions.example

Industry/Entity Type

Business

```html
<!DOCTYPE html>
<html lang="en">
<head>
<meta charset="utf-8">
<title>Moberly Swift Solutions, LLC – Business Card</title>
<link rel="stylesheet" href="https://fonts.googleapis.com/css2?family=Tinos:wght@400;700&display=swap">
<style>
  :root {
    --page-bg: #ffffff;
    --card-bg: #323a3c;
    --muted-teal: #8fb3b0;
    --name-mint: #c9f2e6;
    --mark-blue: #3f8fdc;
  }
  * { margin: 0; padding: 0; box-sizing: border-box; }
  html, body {
    width: 1200px;
    height: 1000px;
    overflow: hidden;
    background: var(--page-bg);
  }
  .card {
    position: absolute;
    left: 77px;
    top: 181px;
    width: 1048px;
    height: 636px;
    background: var(--card-bg);
    font-family: "Tinos", "Times New Roman", serif;
    font-weight: 700;
  }
  .company-line {
    position: absolute;
    right: 20px;
    top: 14px;
    font-size: 37px;
    color: var(--muted-teal);
    white-space: nowrap;
  }
  .brand {
    position: absolute;
    left: 22px;
    top: 200px;
    display: flex;
    align-items: center;
    gap: 30px;
  }
  .brand-dot {
    width: 170px;
    height: 170px;
    flex: none;
  }
  .brand-name {
    font-size: 35px;
    line-height: 50px;
    color: var(--mark-blue);
    white-space: nowrap;
  }
  .person {
    position: absolute;
    left: 608px;
    width: 400px;
    top: 222px;
    text-align: center;
  }
  .person-name {
    font-size: 54px;
    line-height: 66px;
    color: var(--name-mint);
    white-space: nowrap;
  }
  .person-title {
    font-size: 42px;
    line-height: 56px;
    margin-top: 8px;
    color: var(--name-mint);
  }
  .contact {
    position: absolute;
    left: 35px;
    top: 472px;
    list-style: none;
    font-size: 36px;
    line-height: 48px;
    color: var(--muted-teal);
    white-space: nowrap;
  }
</style>
</head>
<body>
  <section class="card">
    <p class="company-line">Moberly Swift Solutions, LLC</p>

    <div class="brand">
      <svg class="brand-dot" viewBox="0 0 170 170" aria-hidden="true">
        <circle cx="85" cy="85" r="80" fill="var(--mark-blue)"/>
      </svg>
      <p class="brand-name">MOBERLY SWIFT<br>SOLUTIONS<br>LLC</p>
    </div>

    <div class="person">
      <h1 class="person-name">Lucia Pembrook</h1>
      <p class="person-title">President</p>
    </div>

    <ul class="contact">
      <li>Phone number: 703-482-1947</li>
      <li>Email: lpembrook@moberlyswiftsolutions.example</li>
      <li>www.moberlyswiftsolutions.example</li>
    </ul>
  </section>
</body>
</html>
```